VELTRA Corp Has New Logo Now Needs New Stationary

We just chose our new logo, and now we need a letterhead and envelope design. I would like both to be used via Microsoft Word so I can print both the letterhead and envelopes myself rather than having to the letterhead and envelopes produced by a printing firm. I has attached the new logo and spec sheet provided by the logo designer.

```html
<!DOCTYPE html>
<html lang="en">
<head>
<meta charset="utf-8">
<title>VELTRA Corp Stationery</title>
<link rel="stylesheet" href="https://fonts.googleapis.com/css2?family=Montserrat:wght@600&family=Open+Sans:wght@400&display=swap">
<style>
  :root {
    --stage: #e9e7e3;
    --paper: #ffffff;
    --paper-edge: #d6d6d6;
    --flap-grey: #f2f2f2;
    --brand-green: #7cbd42;
    --brand-blue: #3aa9e0;
    --ink: #333333;
    --ink-soft: #555555;
  }
  * { box-sizing: border-box; margin: 0; padding: 0; }
  html, body { width: 1200px; height: 700px; overflow: hidden; }
  body {
    position: relative;
    background: var(--stage);
    font-family: "Open Sans", Arial, sans-serif;
    color: var(--ink);
  }
  .sheet {
    position: absolute;
    background: var(--paper);
    border: 1px solid var(--paper-edge);
    overflow: hidden;
  }
  .wave { position: absolute; left: 0; bottom: 0; display: block; }

  .wordmark {
    position: absolute;
    font-family: "Montserrat", Arial, sans-serif;
    font-weight: 600;
    color: var(--ink);
    letter-spacing: -0.5px;
    white-space: nowrap;
  }

  /* Letterhead */
  .letterhead { left: 12px; top: 20px; width: 510px; height: 668px; }
  .letterhead .wordmark { left: 18px; top: 84px; font-size: 27px; }
  .contact-list {
    position: absolute; right: 12px; top: 52px;
    list-style: none; font-size: 10.5px; line-height: 13.5px; color: var(--ink);
  }
  .contact-list li { display: flex; align-items: center; gap: 3px; }
  .contact-list svg { width: 9px; height: 9px; }
  .letterhead .address {
    position: absolute; right: 20px; bottom: 19px; font-size: 10px; color: var(--ink-soft);
  }

  /* Envelope backs */
  .envelope-back { left: 618px; top: 42px; width: 555px; height: 270px; }
  .flap { position: absolute; left: 0; top: 0; }
  .flap-name {
    position: absolute; left: 0; right: 0; top: 30px; text-align: center;
    font-family: "Montserrat", Arial, sans-serif; font-weight: 600; font-size: 22px;
  }
  .envelope-back .flap-name { color: var(--paper); }
  .envelope-inner { left: 585px; top: 155px; width: 558px; height: 270px; }
  .envelope-inner .flap-name { color: var(--brand-green); }

  /* Envelope front */
  .envelope-front { left: 551px; top: 289px; width: 557px; height: 270px; }
  .envelope-front .wordmark { left: 10px; top: 76px; font-size: 25px; }
  .envelope-front .address { position: absolute; left: 14px; top: 121px; font-size: 10px; color: var(--ink-soft); }
  .envelope-front .web {
    position: absolute; right: 24px; bottom: 15px; font-size: 10px; letter-spacing: 1.6px; color: var(--ink);
  }
</style>
</head>
<body>

  <section class="sheet letterhead" aria-label="Letterhead">
    <div class="wordmark">VELTRA CORP</div>
    <ul class="contact-list">
      <li><svg viewBox="0 0 10 10"><circle cx="5" cy="5" r="5" fill="var(--brand-blue)"/></svg>123-456-0789</li>
      <li><svg viewBox="0 0 10 10"><rect x="2.5" y="0.5" width="5" height="9" rx="1" fill="var(--brand-blue)"/></svg>123-456-0789</li>
      <li><svg viewBox="0 0 10 10"><rect x="0.5" y="2" width="9" height="6" rx="1" fill="var(--brand-blue)"/><path d="M1 2.5 L5 5.5 L9 2.5" stroke="#fff" stroke-width="1" fill="none"/></svg>hello@veltrafdn-mail.org</li>
      <li><svg viewBox="0 0 10 10"><circle cx="5" cy="5" r="4.5" fill="var(--brand-blue)"/><path d="M0.5 5 H9.5 M5 0.5 V9.5" stroke="#fff" stroke-width="0.8"/></svg>www.veltrafdn-mail.org</li>
    </ul>
    <svg class="wave" width="510" height="140" viewBox="0 0 510 140" aria-hidden="true">
      <path d="M0 110 Q230 100 440 40 L440 140 L0 140 Z" fill="var(--brand-blue)"/>
      <path d="M0 116 Q260 102 510 4 L510 140 L0 140 Z" fill="var(--paper)"/>
      <path d="M0 122 Q260 108 510 10 L510 140 L0 140 Z" fill="var(--brand-green)"/>
    </svg>
    <p class="address">Street Name, City Name, State Zip Code</p>
  </section>

  <section class="sheet envelope-back" aria-label="Envelope back">
    <svg class="flap" width="555" height="85" viewBox="0 0 555 85" aria-hidden="true">
      <path d="M0 0 H555 V62 L545 85 H10 L0 62 Z" fill="var(--brand-green)"/>
    </svg>
    <div class="flap-name">VELTRA CORP</div>
  </section>

  <section class="sheet envelope-inner" aria-label="Envelope flap">
    <svg class="flap" width="558" height="86" viewBox="0 0 558 86" aria-hidden="true">
      <path d="M0 0 H558 L546 85 H12 Z" fill="var(--flap-grey)" stroke="#cfcfcf" stroke-width="1"/>
    </svg>
    <div class="flap-name">VELTRA CORP</div>
  </section>

  <section class="sheet envelope-front" aria-label="Envelope front">
    <div class="wordmark">VELTRA CORP</div>
    <p class="address">Street Name, City Name, State Zip Code</p>
    <svg class="wave" width="557" height="130" viewBox="0 0 557 130" aria-hidden="true">
      <path d="M0 100 Q260 88 460 30 L460 130 L0 130 Z" fill="var(--brand-blue)"/>
      <path d="M0 106 Q280 90 557 -3 L557 130 L0 130 Z" fill="var(--paper)"/>
      <path d="M0 112 Q280 96 557 3 L557 130 L0 130 Z" fill="var(--brand-green)"/>
    </svg>
    <p class="web">www.veltrafdn-mail.org</p>
  </section>

</body>
</html>
```